Flyer-Design für Pflegedienst
Zielgruppe
Moin liebe Designer,
Wir sind ein ambulanter Intensivpflegedienst im Speckgürtel Hamburgs. Wir betreuen seit über 20 Jahren Kinder, Jugendliche und Erwachsene, die eine dauerhafte Überwachung und Betreuung benötigen. Dabei sind unsere Pflegefachkräfte dauerhaft vor Ort. Wir haben kaum Fluktuation, eine hohe Mitarbeiterzufriedenheit und erhalten auch weiterhin Bewerbungen in diesem hart umkämpften Markt.
Aufgabenstellung
Wir wollen nun in Zukunft unsere Leistungen auf einen Flyer bringen. Dazu würden wir gerne einen Flyer für die ambulante Intensivpflege erstellen lassen, die Informationen sind auf unserer Homepage unter Leistungen zu finden: https://elkor-pflegedienst.de/leistungen/ und es darf gerne ein Standart-Flyer im entsprechendem Format sein.
..und einen Flyer für unsere haushaltsnahen Dienstleistungen. Dazu haben wir die Word-Datei mit den Punkten / Leistungen erstellt und angehängt. Der Flyer soll später als Türanhänger genutzt werden können.
Für die Gestaltung kann gerne auf das bereits vorhandene Material zurück gegriffen werden.

```html
<!DOCTYPE html>
<html lang="de">
<head>
<meta charset="utf-8">
<title>Elkor Pflegedienst – Flyer</title>
<link rel="stylesheet" href="https://fonts.googleapis.com/css2?family=Fira+Sans:wght@600;700&family=Open+Sans:wght@400;600;700&display=swap">
<style>
:root{
  --sky:#5bc8f5;
  --navy:#0b3a63;
  --ink:#1e2a38;
  --magenta:#c461b4;
  --pale:#eaf6fd;
  --photo-a:#d9e6ef;
  --photo-b:#8fb3cc;
  --paper:#ffffff;
  --stage:#f3f4f6;
}
*{margin:0;padding:0;box-sizing:border-box}
html,body{width:1200px;height:1200px;overflow:hidden;background:var(--stage)}
body{position:relative;font-family:"Open Sans",Arial,sans-serif;color:var(--ink)}
.spread{position:absolute;left:196px;width:808px;height:575px;background:var(--paper);overflow:hidden;box-shadow:0 6px 18px rgba(0,0,0,.18)}
.spread--outside{top:14px}
.spread--inside{top:606px}
.spread svg.backdrop{position:absolute;inset:0}
.fold{position:absolute;top:0;bottom:0;width:1px;background:rgba(0,0,0,.06)}
.photo{position:absolute;border-radius:50%;background:radial-gradient(circle at 40% 35%,var(--photo-a),var(--photo-b))}
.photo--warm{background:radial-gradient(circle at 45% 40%,#efe2da,#b69a8c)}
.photo--blue{background:radial-gradient(circle at 50% 55%,#2a56c4,#dfe7ef 68%)}
.photo--beach{background:linear-gradient(#4b9bd8,#bcdcf0 45%,#d9c9a6 60%,#b9a57f)}
.dot{position:absolute;border-radius:50%;background:var(--magenta)}
.ghost{position:absolute;border-radius:50%;background:var(--pale)}
.panel-title{position:absolute;font-family:"Fira Sans",sans-serif;font-weight:700;color:var(--navy);font-size:12px;text-align:center;transform:translateX(-50%);white-space:nowrap}
.kicker{font-family:"Open Sans",sans-serif;font-weight:700;color:var(--magenta);font-size:7.2px;margin-bottom:9px}
.col{position:absolute;font-size:7px;line-height:1.3}
.col p{margin-bottom:8px}
.list{list-style:none}
.list li{position:relative;padding-left:22px;margin-bottom:8px}
.list li::before{content:"";position:absolute;left:2px;top:0;width:14px;height:12px;border:1.5px solid var(--sky);border-radius:50% 50% 40% 40%;opacity:.8}
.headline{position:absolute;font-family:"Fira Sans",sans-serif;font-weight:700;color:var(--navy);text-align:center}
.brand{position:absolute;left:590px;top:40px;display:flex;align-items:center;gap:8px;font-family:"Fira Sans",sans-serif;font-weight:600;color:#fff;font-size:24px;letter-spacing:.5px}
.brand::before{content:"";width:14px;height:14px;border-radius:50%;background:#fff}
.contact{position:absolute;left:287px;top:418px;font-size:7px;line-height:1.3}
.contact p{margin-bottom:8px}
</style>
</head>
<body>

<section class="spread spread--outside" aria-label="Flyer Außenseite">
  <svg class="backdrop" width="808" height="575" viewBox="0 0 808 575" aria-hidden="true">
    <path d="M0 0H808V90C770 118 720 125 650 120C560 114 470 95 390 70C300 45 140 60 0 100Z" fill="var(--sky)"/>
    <path d="M390 70C470 95 560 114 650 120C720 125 770 118 808 90V106C770 134 720 140 650 136C560 130 470 110 390 78Z" fill="var(--navy)"/>
    <path d="M0 525C120 490 250 480 400 500C520 520 600 560 700 555C750 552 790 535 808 520V575H0Z" fill="var(--sky)"/>
  </svg>
  <div class="fold" style="left:266px"></div>
  <div class="fold" style="left:533px"></div>

  <h2 class="panel-title" style="left:133px;top:94px">Pflegedienstleistungen</h2>
  <div class="col" style="left:14px;top:121px;width:240px">
    <div class="kicker">Intensiv- und Grundpflege</div>
    <p>Bei der Intensiv- und Grundpflege unterstützen wir Sie in allen Aktivitäten des täglichen Lebens. Zur Behandlungspflege zählen medizinische Leistungen, die auf ärztliche Verordnung durchgeführt werden.</p>
    <ul class="list">
      <li>Sowohl die Grund- als auch die Behandlungspflege kann Zuhause oder in Wohngemeinschaften stattfinden.</li>
      <li>Bis zu 24 Stunden lösungs- und situativorientierte, intensiv-pflegerische Betreuung</li>
      <li>Beatmungsintensivpflege (invasive und nicht-invasive Beatmung)</li>
      <li>Überwachung der Vitalfunktionen / Monitoring</li>
      <li>Pflegeberatung zu den Leistungen der Pflegekasse und Finanzierung der Pflege (Beratungsbesuch nach § 37 Abs.3 SGB XI (Nachweis für die Pflegekasse ab Pflegegrad 2-5))</li>
      <li>Unterstützung bei Ihren Verordnungen und bei der Sterbebegleitung</li>
    </ul>
  </div>
  <div class="photo photo--warm" style="left:70px;top:392px;width:150px;height:150px" role="img" aria-label="Foto: Hand eines Patienten mit Infusionszugang"></div>
  <div class="dot" style="left:47px;top:469px;width:56px;height:56px"></div>
  <div class="dot" style="left:181px;top:398px;width:28px;height:28px"></div>

  <div class="photo photo--warm" style="left:388px;top:33px;width:124px;height:124px" role="img" aria-label="Foto: lächelnde Pflegekraft im Gespräch"></div>
  <div class="ghost" style="left:293px;top:143px;width:88px;height:88px"></div>
  <div class="ghost" style="left:398px;top:258px;width:88px;height:88px"></div>
  <h1 class="headline" style="left:276px;top:204px;width:248px;font-size:17.5px;line-height:1.18">Nehmen Sie jetzt Kontakt zu uns auf und lassen uns darüber sprechen, wie wir Sie unterstützen können.</h1>
  <div class="contact">
    <p>Elkor Pflegedienst<br>Lindenweg 17 B<br>21218 Musterau</p>
    <p>040 / 55 0123 480<br>info@elkor-pflegedienst.de</p>
  </div>
  <div class="dot" style="left:392px;top:480px;width:64px;height:64px"></div>
  <div class="dot" style="left:464px;top:513px;width:34px;height:34px"></div>

  <div class="brand">Elkor Pflegedienst</div>
  <h2 class="headline" style="left:543px;top:158px;width:260px;font-size:19px;line-height:1.25">Unsere<br>Pflegeleistungen</h2>
  <div class="photo photo--blue" style="left:550px;top:210px;width:262px;height:282px" role="img" aria-label="Foto: lächelnde Pflegerin in blauer Dienstkleidung"></div>
  <div class="headline" style="left:543px;top:505px;width:260px;font-size:17px">Wir unterstützen Sie</div>
  <div class="dot" style="left:708px;top:541px;width:24px;height:24px"></div>
  <div class="dot" style="left:748px;top:538px;width:20px;height:20px"></div>
  <div class="dot" style="left:774px;top:526px;width:16px;height:16px"></div>
</section>

<section class="spread spread--inside" aria-label="Flyer Innenseite">
  <svg class="backdrop" width="808" height="575" viewBox="0 0 808 575" aria-hidden="true">
    <path d="M0 0H808V100C740 90 640 75 560 72C460 70 380 80 300 90C230 95 150 70 60 58C40 56 20 58 0 62Z" fill="var(--sky)"/>
    <path d="M0 62C60 58 150 72 240 92L240 98C150 82 60 70 0 72Z" fill="var(--navy)"/>
    <path d="M290 92C380 80 460 70 560 72C640 75 740 92 808 102V114C740 104 640 86 560 84C460 84 380 92 290 98Z" fill="var(--navy)"/>
    <path d="M0 492C80 488 160 500 250 515C340 528 420 505 500 498C580 492 660 520 808 498V575H0Z" fill="var(--sky)"/>
  </svg>
  <div class="fold" style="left:270px"></div>
  <div class="fold" style="left:540px"></div>

  <div class="photo photo--warm" style="left:-2px;top:13px;width:90px;height:90px" role="img" aria-label="Foto: Pflegerin mit Kind"></div>
  <div class="dot" style="left:165px;top:67px;width:14px;height:14px"></div>
  <div class="dot" style="left:197px;top:67px;width:26px;height:26px"></div>
  <div class="dot" style="left:242px;top:64px;width:50px;height:50px"></div>
  <div class="dot" style="left:452px;top:34px;width:46px;height:46px"></div>
  <div class="photo" style="left:488px;top:8px;width:94px;height:94px" role="img" aria-label="Foto: Betreuung eines Kindes im Alltag"></div>
  <div class="dot" style="left:578px;top:57px;width:20px;height:20px"></div>

  <h2 class="panel-title" style="left:135px;top:94px">Alltagshilfe</h2>
  <div class="col" style="left:14px;top:121px;width:242px">
    <div class="kicker">Bewahren Sie sich Ihre Alltagsroutinen – mit unserer Hilfe</div>
    <p>Im Alltag mit seinen immer neuen Herausforderungen ist es für unsere Patient:innen wichtig, eine verlässliche Unterstützung zu haben.</p>
    <p>Unsere Angebote in diesem Bereich:</p>
    <ul class="list">
      <li>Haushalts- &amp; Einkaufshilfe (über den Entlastungsbetrag der Pflegekasse möglich)</li>
      <li>Unterstützung der individuellen Lebensgestaltung</li>
      <li>Urlaubsbegleitung</li>
      <li>Begleitung zu kulturellen und Freizeitveranstaltungen</li>
      <li>Schulbegleitung &amp; Begleitung zum Arbeitsplatz</li>
      <li>Vermittlung von ehrenamtlichen Helfern für diverse Besorgungen</li>
      <li>Demnächst bieten wir Ihnen auch einen eigenen Fahrdienst mit behindertengerechten Fahrzeugen an. Sprechen Sie uns gern darauf an!</li>
    </ul>
  </div>

  <h2 class="panel-title" style="left:406px;top:94px">Betreuung</h2>
  <div class="col" style="left:285px;top:121px;width:242px">
    <div class="kicker">Wir sind für Sie da</div>
    <p>Es ist ein gutes Gefühl zu wissen, dass immer jemand in der Nähe ist, um sich zu kümmern. Nutzen Sie unser Angebot vor Ort, um Ihre Selbstständigkeit zu erhalten:</p>
    <ul class="list">
      <li>24 Stunden Rufbereitschaft</li>
      <li>Angehörigenbetreuung &amp; -schulung</li>
      <li>Ausstattung mit Hausnotrufsystemen</li>
      <li>Schulungen &amp; Anleitung zur Selbstständigkeit unserer Patienten:innen vor Ort</li>
    </ul>
  </div>
  <h2 class="panel-title" style="left:406px;top:274px">Qualitätssicherung</h2>
  <div class="col" style="left:285px;top:302px;width:242px">
    <div class="kicker">Pflege auf höchstem Niveau – immer</div>
    <p>Als Intensiv-Pflegedienst arbeiten wir in einem sehr dynamischen Bereich, in dem es oft Neuerungen gibt und es auf eine gute Kommunikation ankommt.</p>
    <p>Was Sie von uns erwarten können:</p>
    <ul class="list">
      <li>Individuell zusammengestellte Pflegeteams nach Ihren Bedürfnissen</li>
      <li>Regelmäßige innerbetriebliche Besprechungen &amp; Fortbildungen der Pflegefachkräfte</li>
      <li>Regelmäßige Besuche der Leitung vor Ort</li>
      <li>Unterstützung als Bindeglied zwischen Patient:innen, Kranken- &amp; Pflegekasse</li>
    </ul>
  </div>

  <h2 class="panel-title" style="left:677px;top:94px">Beratung</h2>
  <div class="col" style="left:556px;top:121px;width:242px">
    <div class="kicker">Wir reden miteinander</div>
    <p>Wenn eine Pflegesituation entsteht oder sich ändert, unterstützen wir unsere Patient:innen und deren Angehörigen optimale Lösungen zu finden.</p>
    <ul class="list">
      <li>Technisch &amp; fachlich fundierte Beratung zu Kranken- &amp; Pflegekassenanträgen</li>
      <li>Zusammenarbeit mit den Selbsthilfegruppen ALS und IGA</li>
      <li>Kooperative Zusammenarbeit mit Ärzt:innen, Therapeut:innen, Medizintechnikfirmen und anderen an der Pflege beteiligten Personen</li>
    </ul>
  </div>
  <h2 class="panel-title" style="left:677px;top:274px">Erholung</h2>
  <div class="col" style="left:556px;top:302px;width:242px">
    <div class="kicker">Wir unterstützen Sie bei der Urlaubsplanung</div>
    <p>Auch als Pflegebedürftige:r möchte man mal raus aus dem Alltag und was erleben. Das ist möglich, wenn man ein paar Dinge beachtet. Lassen Sie sich dazu gern von uns unterstützen.</p>
    <ul class="list">
      <li>Beratung zu geeigneten barrierefreien Reisezielen</li>
      <li>Vermittlung &amp; Vermietung von Ferienhäusern &amp; Wohnungen in Deutschland</li>
      <li>Empfehlung von geeigneten Reiseanbietern in Deutschland und im Ausland</li>
    </ul>
  </div>

  <div class="photo photo--warm" style="left:82px;top:386px;width:92px;height:92px" role="img" aria-label="Foto: Hände als Zeichen des Zusammenhalts"></div>
  <div class="dot" style="left:60px;top:448px;width:36px;height:36px"></div>
  <div class="photo" style="left:146px;top:426px;width:134px;height:134px" role="img" aria-label="Foto: Seniorin mit Betreuerin am Laptop"></div>
  <div class="dot" style="left:273px;top:509px;width:22px;height:22px"></div>
  <div class="dot" style="left:480px;top:482px;width:15px;height:15px"></div>
  <div class="photo" style="left:500px;top:448px;width:136px;height:136px" role="img" aria-label="Foto: zwei Pflegekräfte im Team"></div>
  <div class="dot" style="left:653px;top:498px;width:26px;height:26px"></div>
  <div class="dot" style="left:696px;top:493px;width:52px;height:52px"></div>
  <div class="photo photo--beach" style="left:718px;top:425px;width:110px;height:110px" role="img" aria-label="Foto: Strandweg an der Küste"></div>
</section>

</body>
</html>
```